KB Rubbish Removal Business Card

Hey,
I need a double sided business card designed for a rubbish removal business based in Australia. Logo is already chosen, similar colours preferred for both sides of the business card.

Details to include:

Front:

KB Rubbish Removal
Darren Holloway
Managing Director
Mobile: 0471 902 146
Email: darren@kbrubbishremoval.com.au
Website: kbrubbishremoval.com.au

Rear:

How did we do?
kbrubbishremoval.com.au/review

```html
<!DOCTYPE html>
<html lang="en">
<head>
<meta charset="utf-8">
<title>KB Rubbish Removal Business Card</title>
<link href="https://fonts.googleapis.com/css2?family=Poppins:ital,wght@0,400;0,500;0,600;0,700;1,400&display=swap" rel="stylesheet">
<style>
  :root {
    --brand-green: #0e8a22;
    --leaf-green: #2fb84a;
    --paper: #ffffff;
    --page-light: #fdfdfd;
  }
  * { margin: 0; padding: 0; box-sizing: border-box; }
  html, body { width: 1200px; height: 1199px; overflow: hidden; }
  body { position: relative; font-family: "Poppins", sans-serif; background: var(--page-light); }

  .rear-stage { position: absolute; left: 0; top: 0; width: 1200px; height: 599px; background: var(--page-light); }
  .front-stage { position: absolute; left: 0; top: 599px; width: 1200px; height: 600px; background: var(--brand-green); }

  .card-rear {
    position: absolute; left: 329px; top: 136px; width: 542px; height: 326px;
    background: var(--brand-green); color: var(--paper); text-align: center;
  }
  .review-heading {
    position: absolute; left: 0; right: 0; top: 108px;
    font-weight: 700; font-size: 61px; line-height: 1; letter-spacing: -0.5px;
  }
  .review-url {
    position: absolute; left: 0; right: 0; top: 181px;
    font-style: italic; font-weight: 400; font-size: 24px; line-height: 1;
  }

  .card-front {
    position: absolute; left: 328px; top: 136px; width: 543px; height: 327px;
    background: var(--paper); color: var(--brand-green); overflow: hidden;
  }
  .company-name {
    position: absolute; left: 29px; top: 62px;
    font-weight: 700; font-size: 30px; line-height: 1; letter-spacing: -0.3px;
  }
  .person { position: absolute; left: 35px; top: 136px; }
  .person-name { font-weight: 600; font-size: 21px; line-height: 1; }
  .person-title { font-weight: 400; font-size: 13px; line-height: 1.2; margin-top: 1px; }
  .person-rule { position: absolute; left: 36px; top: 178px; width: 191px; height: 1.5px; background: var(--brand-green); }

  .contact-list { position: absolute; left: 32px; top: 215px; list-style: none; }
  .contact-item { display: flex; align-items: center; height: 21px; margin-bottom: 6.5px; }
  .contact-icon { width: 21px; height: 21px; flex: none; margin-right: 5px; }
  .contact-text { font-weight: 500; font-size: 9.5px; line-height: 1; }

  .brand-mark {
    position: absolute; left: 340px; top: 122px; width: 180px; height: 180px;
    border-radius: 50%; background: linear-gradient(135deg, #62c846, var(--leaf-green) 50%, #129a36);
  }
</style>
</head>
<body>
  <section class="rear-stage">
    <div class="card-rear">
      <h1 class="review-heading">How did we do?</h1>
      <p class="review-url">kbrubbishremoval.com.au/review</p>
    </div>
  </section>

  <section class="front-stage">
    <div class="card-front">
      <h2 class="company-name">KB Rubbish Removal</h2>
      <div class="person">
        <p class="person-name">Darren Holloway</p>
        <p class="person-title">Managing Director</p>
      </div>
      <div class="person-rule"></div>

      <ul class="contact-list">
        <li class="contact-item">
          <svg class="contact-icon" viewBox="0 0 21 21" aria-hidden="true">
            <circle cx="10.5" cy="10.5" r="9.7" fill="none" stroke="#0e8a22" stroke-width="1.2"/>
            <rect x="7.5" y="5" width="6" height="11" rx="1" fill="none" stroke="#0e8a22" stroke-width="1.1"/>
            <circle cx="10.5" cy="14" r="0.7" fill="#0e8a22"/>
          </svg>
          <span class="contact-text">0471 902 146</span>
        </li>
        <li class="contact-item">
          <svg class="contact-icon" viewBox="0 0 21 21" aria-hidden="true">
            <circle cx="10.5" cy="10.5" r="9.7" fill="none" stroke="#0e8a22" stroke-width="1.2"/>
            <rect x="5.5" y="7" width="10" height="7" fill="none" stroke="#0e8a22" stroke-width="1.1"/>
            <path d="M5.5 7 L10.5 11 L15.5 7 M5.5 14 L9 10.5 M15.5 14 L12 10.5" fill="none" stroke="#0e8a22" stroke-width="1"/>
          </svg>
          <span class="contact-text">darren@kbrubbishremoval.com.au</span>
        </li>
        <li class="contact-item">
          <svg class="contact-icon" viewBox="0 0 21 21" aria-hidden="true">
            <circle cx="10.5" cy="10.5" r="9.7" fill="none" stroke="#0e8a22" stroke-width="1.2"/>
            <circle cx="9.5" cy="9.5" r="3.5" fill="none" stroke="#0e8a22" stroke-width="1.1"/>
            <path d="M12 12 L15.5 15.5" stroke="#0e8a22" stroke-width="1.4" stroke-linecap="round"/>
          </svg>
          <span class="contact-text">kbrubbishremoval.com.au</span>
        </li>
      </ul>

      <div class="brand-mark" role="img" aria-label="KB Rubbish Removal brand mark"></div>
    </div>
  </section>
</body>
</html>
```